Searching for a captivating trade show banner design that captures the audience's attention.

I am looking to have someone design pop up trade show banner to go with my business card and flyer. Must be high resolution to print larger. See attached pics

I extended the timelines on this project.

Target Market(s)

Any commercial facility that would have fitness equipment. Park and Recreation, Fitness Centers, Multi-family, schools

Industry/Entity Type

Fitness space design and planning. fitness equipment sales. High end clients

Colors
0054AA
0677BA
7BADD7
CADEEF
E8F1F8

Requirements
Must have
• Similar look to attached business card and flyer. I would like to try and get custom look to brand. Unique cool design. I do high end facility so some type of architecture elements and or look.
Nice to have
• the smaller logo like the back of my business card somewhere on the banner design
Should not have
• clutter, dark and hard to read

```html
<!DOCTYPE html>
<html lang="en">
<head>
<meta charset="utf-8">
<title>Strength In Form – Pull-up Banner</title>
<link rel="stylesheet" href="https://fonts.googleapis.com/css2?family=Maven+Pro:wght@400;500&family=Saira:ital,wght@0,500;1,500;1,700&display=swap">
<style>
  :root{
    --stage:#ececef;
    --banner:#2a2a2b;
    --blue:#0096db;
    --light-blue:#7badd7;
    --white:#ffffff;
    --pattern:#4a4a4c;
  }
  *{margin:0;padding:0;box-sizing:border-box}
  html,body{width:1200px;height:1200px;overflow:hidden;background:var(--stage)}
  .banner{
    position:absolute;left:325px;top:20px;width:550px;height:1160px;
    background:var(--banner);overflow:hidden;
    font-family:"Maven Pro",sans-serif;color:var(--white);
  }
  .pattern-band{
    position:absolute;left:260px;top:0;width:290px;height:102px;
    background:linear-gradient(90deg,rgba(74,74,76,0) 0%,var(--pattern) 70%,#58585a 100%);
    opacity:.7;
  }
  .brand-vertical{position:absolute;left:40px;top:100px;width:80px;height:920px}
  .brand-vertical text{font-family:"Saira",sans-serif;font-weight:500;fill:var(--white)}
  .services{position:absolute;right:0;top:0;width:100%;height:100%}
  .service{
    position:absolute;right:97px;text-align:right;line-height:1.05;
  }
  .service .lead{display:block;font-size:24px;font-weight:400}
  .service .main{display:block;font-size:30px;font-weight:400}
  .service-icon{position:absolute;left:470px;width:46px;height:46px}
  .service-icon *{stroke:var(--blue);fill:none;stroke-width:2.2;stroke-linecap:round;stroke-linejoin:round}
  .service-icon .solid{fill:var(--blue);stroke:none}
  .brand-mark{
    position:absolute;left:270px;top:885px;width:250px;
    display:flex;align-items:center;gap:12px;
  }
  .brand-mark .square{width:34px;height:34px;background:var(--blue);flex:none}
  .brand-mark .name{font-family:"Maven Pro",sans-serif;font-weight:500;font-size:24px;color:var(--white);line-height:1.1}
  .contact{
    position:absolute;left:52px;top:1064px;display:flex;align-items:center;gap:24px;
    font-size:20px;
  }
  .contact span{display:flex;align-items:center;gap:5px}
  .contact svg{width:20px;height:18px}
  .web{
    position:absolute;left:52px;top:1094px;width:452px;
    font-family:"Saira",sans-serif;font-style:italic;font-weight:700;font-size:33px;letter-spacing:.5px;
    white-space:nowrap;
  }
  .web .domain{color:var(--light-blue)}
</style>
</head>
<body>
<main class="banner">
  <div class="pattern-band" role="img" aria-label="Faint repeating brand monogram pattern"></div>

  <svg class="brand-vertical" viewBox="0 0 80 920">
    <text transform="translate(72 913) rotate(-90)" font-size="78" textLength="905" lengthAdjust="spacingAndGlyphs">STRENGTH IN FORM</text>
  </svg>

  <section class="services">
    <p class="service" style="top:204px"><span class="lead">Conceptual</span><span class="main">Planing</span></p>
    <svg class="service-icon" style="top:218px" viewBox="0 0 46 46">
      <path d="M14 30 L36 8 L41 13 L19 35 L12 37 Z"/><rect x="4" y="28" width="14" height="14"/><rect x="7" y="35" width="6" height="6"/>
    </svg>

    <p class="service" style="top:334px"><span class="lead">Equipment</span><span class="main">Specifications</span></p>
    <svg class="service-icon" style="top:346px" viewBox="0 0 46 46">
      <circle cx="23" cy="8" r="4"/><line x1="23" y1="12" x2="23" y2="40"/><circle cx="23" cy="38" r="5"/>
      <line x1="2" y1="20" x2="14" y2="20"/><line x1="2" y1="27" x2="14" y2="27"/><line x1="2" y1="34" x2="14" y2="34"/>
      <line x1="32" y1="20" x2="44" y2="20"/><line x1="32" y1="27" x2="44" y2="27"/><line x1="32" y1="34" x2="44" y2="34"/>
    </svg>

    <p class="service" style="top:465px"><span class="lead">Procurement</span><span class="main">Equipment</span></p>
    <svg class="service-icon" style="top:472px" viewBox="0 0 46 46">
      <rect class="solid" x="2" y="38" width="40" height="5"/><line x1="34" y1="38" x2="38" y2="6"/><line x1="20" y1="14" x2="40" y2="10"/><line x1="28" y1="22" x2="36" y2="22"/>
    </svg>

    <p class="service" style="top:596px"><span class="lead">3rd Party</span><span class="main">Collaboration</span></p>
    <svg class="service-icon" style="top:604px" viewBox="0 0 46 46">
      <circle cx="26" cy="18" r="15"/><ellipse cx="26" cy="18" rx="6" ry="15"/><line x1="11" y1="18" x2="41" y2="18"/>
      <circle class="solid" cx="16" cy="26" r="6"/><path class="solid" d="M4 42 Q16 28 28 42 Z"/>
    </svg>

    <p class="service" style="top:726px"><span class="lead">Preventative</span><span class="main">Maintenance Service</span></p>
    <svg class="service-icon" style="top:736px" viewBox="0 0 46 46">
      <circle cx="23" cy="23" r="12" stroke-width="6" stroke-dasharray="5 4"/><circle cx="23" cy="23" r="6"/><line x1="27" y1="27" x2="38" y2="38" stroke-width="3"/>
    </svg>
  </section>

  <div class="brand-mark">
    <span class="square"></span>
    <span class="name">Strength In Form</span>
  </div>

  <div class="contact">
    <span><svg viewBox="0 0 20 18"><path d="M4 1 L8 5 L6 8 Q9 12 12 13 L15 10 L19 14 L16 17 Q6 16 2 4 Z" fill="var(--light-blue)"/></svg>555 014 2870</span>
    <span><svg viewBox="0 0 20 18"><rect x="1" y="3" width="18" height="13" fill="var(--light-blue)"/><path d="M1 3 L10 10 L19 3" stroke="var(--banner)" stroke-width="1.5" fill="none"/></svg>Dana@strengthinform.co</span>
  </div>

  <p class="web">www.<span class="domain">strengthinform</span>.co</p>
</main>
</body>
</html>
```